Promotional Flyer/Email Design - Cabling services for Broadcast and Audio Visual

We need a promotional flyer/email design to help launch our company, Velto Wire. We provide cabling services for Broadcast Television and Audio Visual systems. Recent projects include major television events such as the Harrowfield Racquet Open and Audio Visual/Entertainment systems for wealthy clients in their homes and on-board super yachts.

The flyer will be printed as single sided A5 and also be sent out in the body of a promotional email. It should feature the company logo along with a complementary colour scheme. It should have a clean finish with images that show the type of work we do (cabling and equipment installation) or the setting for these systems (tv studio, super yacht, cinema room, meeting room with projector etc.)

Services we offer are:

Broadcast/AV system design
On-site installation
Rack building
Pre-fabricated cable looms
Fibre optic installation

About the company:

Velto Wire provide cabling services for Broadcast Television and Audio Visual systems. With over 15 years experience working in these industries we can help with every aspect of design, project managment, installation and maintenance. Our projects range from fibre optic cabling at major sports events to installing and commisioning bespoke control systems on some of the worlds largest super yachts.

Contact details:

To get a quote or discuss your project contact us now
Telephone: TBC
Email: info@velto-wire.example
Website: www.velto-wire.example
Address: TBC

Other information:

The company is based in London, UK. Our projects often take place in other countries with work taking place accross Europe and beyond.

We have a London based workshop for rack building and cable pre-fabrication.

Our website is www.velto-wire.example

Images:

Images attached can be editted for use on the flyer or have ideas taken from them. Only the company logo is required to feature on the final design.

Target Market(s)

Business to business

Industry/Entity Type

It Company

Font styles to use
Sans Serif

Requirements
Must have
• Company logo
• List of services
• Contact details
Nice to have
• Image of cabling, home cinema room, super yacht, luxury home, outside broadcast truck, fibre optic equipment or cabling.

```html
<!DOCTYPE html>
<html lang="en">
<head>
<meta charset="utf-8">
<title>Velto Wire – Cabling services flyer</title>
<link href="https://fonts.googleapis.com/css2?family=Source+Sans+3:wght@300;400;600;700&display=swap" rel="stylesheet">
<style>
  :root{
    --page:#ffffff;
    --panel:#f6f6f7;
    --yellow:#f6e51c;
    --red:#e4203f;
    --blue:#3f77c0;
    --sky:#1796d2;
    --pale:#a9dbe6;
    --ink:#2b2b2b;
    --grey-ring:#cfd0d3;
  }
  *{margin:0;padding:0;box-sizing:border-box}
  html,body{width:866px;height:1200px;overflow:hidden;background:var(--page)}
  body{font-family:"Source Sans 3",Arial,sans-serif;color:var(--ink)}
  .flyer{position:relative;width:866px;height:1200px;overflow:hidden}
  .panel{position:absolute;left:19px;top:14px;width:829px;height:1166px;background:var(--panel)}
  .hero{position:absolute;left:0;top:0}
  .headline{position:absolute;left:53px;top:82px;color:var(--yellow);font-weight:700;font-size:38px;line-height:48px;text-shadow:1px 2px 3px rgba(0,0,0,.55)}
  .badge{position:absolute;left:477px;top:332px;width:304px;height:304px;text-align:center}
  .brand{position:absolute;left:0;width:100%;top:120px;font-size:40px;font-weight:700;color:var(--ink);letter-spacing:-.5px;display:flex;align-items:center;justify-content:center;gap:10px}
  .brand-dot{width:18px;height:18px;border-radius:50%;background:var(--red)}
  .badge-email{position:absolute;left:0;width:100%;top:192px;font-size:17px;font-weight:700;color:var(--red)}
  .badge-address{position:absolute;left:0;width:100%;top:223px;font-size:14.5px;line-height:18px;color:var(--ink)}
  .services-title{position:absolute;left:76px;top:622px;font-size:36px;font-weight:300;color:var(--red)}
  .services{position:absolute;left:76px;top:684px;list-style:none}
  .services li{position:relative;padding-left:28px;font-size:20.5px;font-weight:600;color:#333;height:33px;line-height:30px}
  .services li::before{content:"";position:absolute;left:0;top:9px;width:13px;height:13px;border-radius:50%;background:var(--red)}
  .divider{position:absolute;left:405px;top:668px;width:1px;height:212px;background:#b9b9b9}
  .contact{position:absolute;left:445px;top:660px;width:400px}
  .contact-lead{font-size:26px;font-weight:700;line-height:32px;color:#333}
  .phone{margin-top:8px;font-size:42px;font-weight:700;color:var(--red);line-height:50px}
  .contact-email{margin-top:8px;font-size:17px;line-height:26px}
  .contact-address{font-size:17px;line-height:26px;margin-left:-2px}
  .web{margin-top:6px;font-size:23px;font-weight:700;color:var(--blue)}
  .about-title{position:absolute;left:77px;top:876px;font-size:23px;font-weight:700;color:var(--blue)}
  .about{position:absolute;left:77px;top:918px;width:726px;font-size:15.2px;line-height:21px;text-align:justify;color:#333}
  .gallery-item{position:absolute;top:1016px;height:164px}
  .g1{left:18px;width:252px;background:linear-gradient(160deg,#b7a58a,#6d5d4b 60%,#3c342c)}
  .g2{left:279px;width:271px;background:linear-gradient(180deg,#3a3e45,#b9bcc2 45%,#8a8d93)}
  .g3{left:558px;width:144px;background:linear-gradient(100deg,#9fa3a8,#2a2c30 55%,#141518)}
  .g4{left:705px;width:143px;background:linear-gradient(180deg,#2b2e31,#3e4a44 50%,#1c1e20)}
</style>
</head>
<body>
<div class="flyer">
  <div class="panel"></div>

  <svg class="hero" width="866" height="640" viewBox="0 0 866 640" aria-hidden="false">
    <defs>
      <linearGradient id="cinema" x1="0" y1="0" x2="1" y2="1">
        <stop offset="0" stop-color="#8a7a55"/>
        <stop offset=".45" stop-color="#6f6353"/>
        <stop offset="1" stop-color="#3e342d"/>
      </linearGradient>
    </defs>
    <path d="M19,440 L19,528 Q210,610 420,596 Q560,585 650,520 L650,440 Z" fill="var(--blue)"/>
    <path d="M740,340 Q830,180 800,14 L848,14 L848,40 Q845,250 740,400 Z" fill="var(--blue)"/>
    <path d="M760,14 Q860,160 770,380" fill="none" stroke="var(--sky)" stroke-width="14"/>
    <path d="M740,14 Q850,170 760,385" fill="none" stroke="var(--pale)" stroke-width="10"/>
    <path d="M700,14 Q840,160 752,385" fill="none" stroke="var(--red)" stroke-width="22"/>
    <path role="img" aria-label="Photo of a home cinema room with a large projection screen, curtains and reclining seats"
          d="M19,14 H680 Q820,150 742,390 L600,470 Q320,560 19,478 Z" fill="url(#cinema)"/>
    <circle cx="629" cy="484" r="153" fill="var(--grey-ring)"/>
    <circle cx="629" cy="484" r="144" fill="#ffffff"/>
  </svg>

  <h1 class="headline">Cabling<br>services for<br>Broadcast<br>Television and<br>Audio Visual<br>systems</h1>

  <div class="badge">
    <div class="brand"><span class="brand-dot"></span>Velto Wire</div>
    <div class="badge-email">info@velto-wire.example</div>
    <div class="badge-address">Address, Address Address,<br>Address, Address</div>
  </div>

  <h2 class="services-title">Services:</h2>
  <ul class="services">
    <li>Broadcast/AV system design</li>
    <li>On-site installation</li>
    <li>Rack building</li>
    <li>Pre-fabricated cable looms</li>
    <li>Fibre optic installation</li>
  </ul>

  <div class="divider"></div>

  <div class="contact">
    <p class="contact-lead">To get a quote or discuss your project Contact us now</p>
    <p class="phone">07700 900 318</p>
    <p class="contact-email">info@velto-wire.example</p>
    <p class="contact-address">Address, Address, Address, Address, Address</p>
    <p class="web">www.velto-wire.example</p>
  </div>

  <h2 class="about-title">About the company:</h2>
  <p class="about">Velto Wire provide cabling services for Broadcast Television and Audio Visual systems. With over 15 years experience working in these industries we can help with every aspect of design, project managment, installation and maintenance. Our projects range from fibre optic cabling at major sports events to installing and commisioning bespoke control systems on some of the worlds largest super yachts.</p>

  <div class="gallery-item g1" role="img" aria-label="Photo of a luxury living room with a wall-mounted television"></div>
  <div class="gallery-item g2" role="img" aria-label="Photo of a large television studio with a lighting gallery"></div>
  <div class="gallery-item g3" role="img" aria-label="Photo of equipment racks with neat cabling"></div>
  <div class="gallery-item g4" role="img" aria-label="Photo of a rack of patch panels with coloured cables"></div>
</div>
</body>
</html>
```